Drumlin heating company

we are a renewable energy provider that specialise in Biomass
we want to promote our business in the rural and agricultural areas.
I have attached a document with the word content that needs to be on each side, they are specific and need to be exactly whats written. each page relates to each side of the flyer, one is for domestic biomass and one is for commercial biomass, my company logo is attached and so is the manufacturers logo and a picture of the boilers we install. my website is www.drumlinheatingcompany.com if you need to see our general image/branding.
rural / agricultural / off grid.
Business

```html
<!DOCTYPE html>
<html lang="en">
<head>
<meta charset="utf-8">
<title>Drumlin heating company – Commercial RHI</title>
<link href="https://fonts.googleapis.com/css2?family=Roboto:wght@400;500;700;900&display=swap" rel="stylesheet">
<style>
  :root {
    --brand-red: #e52421;
    --ink: #1a1a1a;
    --paper: #ffffff;
    --brand-green: #3fae49;
    --fire-dark: #0b0604;
    --fire-mid: #7a2a08;
    --fire-hot: #f08a1c;
  }
  * { margin: 0; padding: 0; box-sizing: border-box; }
  html, body { width: 850px; height: 1200px; overflow: hidden; background: var(--paper); }
  .flyer {
    position: relative; width: 850px; height: 1200px; overflow: hidden;
    background: var(--paper); color: var(--ink);
    font-family: "Roboto", Arial, sans-serif;
  }
  .quote-mark {
    position: absolute; left: 38px; top: 22px;
    font: 900 78px/1 "Roboto", Arial, sans-serif; color: var(--ink);
  }
  .headline {
    position: absolute; left: 100px; top: 64px;
    font-size: 37px; font-weight: 700; color: var(--brand-red); letter-spacing: -0.3px;
  }
  .intro {
    position: absolute; left: 100px; top: 128px; width: 700px;
    font-size: 18.5px; line-height: 1.5;
  }
  .claim-band {
    position: absolute; left: 0; width: 850px; height: 14px; background: var(--brand-red);
  }
  .claim-band.short { width: 210px; }
  .claim {
    position: absolute; left: 200px; padding: 0 14px;
    background: var(--paper); font-size: 29px; font-weight: 700; line-height: 40px;
  }
  .fixed-price {
    position: absolute; left: 116px; top: 394px;
    font-size: 23.5px; font-weight: 500; color: var(--brand-red);
  }
  .qualify-title {
    position: absolute; left: 170px; top: 452px;
    font-size: 20px; font-weight: 700;
  }
  .criteria { position: absolute; left: 100px; top: 490px; width: 540px; list-style: none; }
  .criteria li {
    position: relative; padding-left: 26px; margin-bottom: 20px;
    font-size: 17.5px; line-height: 1.45;
  }
  .criteria li::before {
    content: ">"; position: absolute; left: 0; top: 0;
    color: var(--brand-red); font-weight: 700;
  }
  .call-to-action {
    position: absolute; left: 126px; top: 880px; width: 520px;
    font-size: 15px; line-height: 1.4; color: var(--brand-red); text-transform: uppercase;
  }
  .maker-name {
    position: absolute; left: 640px; top: 450px;
    font-size: 38px; font-weight: 700; color: var(--brand-red);
  }
  .boiler-photo {
    position: absolute; left: 645px; top: 500px; width: 200px; height: 500px;
    background: linear-gradient(90deg, #f3f3f3 0%, #d9d9d9 45%, var(--brand-red) 46%, #b71c1a 100%);
    border-radius: 4px;
  }
  .fire-photo {
    position: absolute; left: 0; top: 930px; width: 850px; height: 270px;
    background: linear-gradient(180deg, var(--paper) 0%, var(--fire-dark) 22%, var(--fire-mid) 65%, var(--fire-hot) 100%);
  }
  .company-mark {
    position: absolute; left: 46px; top: 960px; display: flex; align-items: center; gap: 12px;
  }
  .company-mark .dot { width: 30px; height: 30px; border-radius: 50%; background: var(--brand-green); }
  .company-mark .name { font-size: 24px; font-weight: 500; color: var(--brand-green); }
</style>
</head>
<body>
<main class="flyer">
  <div class="quote-mark">”</div>
  <h1 class="headline">The Commercial Renewable Heat Incentive</h1>
  <p class="intro">If you invest in a new Biomass boiler for your business or small holding you will be eligible for a 20 year income from the government.<br>For every kilowatt of green energy you burn you will be paid 8.4p plus RPI for the next 20 years!</p>

  <div class="claim-band" style="top:294px"></div>
  <div class="claim" style="top:281px">Biomass is cheaper than mains gas</div>
  <div class="claim-band" style="top:333px"></div>
  <div class="claim" style="top:320px">It's 40% cheaper than Heating Oil</div>
  <div class="claim-band short" style="top:372px"></div>
  <div class="claim" style="top:359px; background:transparent">and 50% cheaper than LPG</div>

  <p class="fixed-price">and we can fix the cost of your biomass pellet fuel supply for 5 years!</p>
  <h2 class="qualify-title">What qualifies for the commercial 20 year RHI?</h2>

  <ul class="criteria">
    <li>If you are a registered business you are eligible for the 20 year RHI</li>
    <li>If you have two or more domestic properties that are separately council taxed are heated by separate heat circuits</li>
    <li>This lucrative RHI is available on boilers up to 199kw!</li>
    <li>Typical installation cost - 60kw Alpfeld PelletMax boiler in purpose built plant room with pellet store &amp; automated pellet feed = £45K</li>
    <li>Typical 20 year income from the RHI = £180K!!</li>
    <li>Typical savings on heating costs over 20 years ( from LPG ) = £180K!!</li>
  </ul>

  <p class="call-to-action">Call us today to find out how you can take advantage of this very lucrative government backed scheme!!</p>

  <div class="maker-name">Alpfeld</div>
  <div class="boiler-photo" role="img" aria-label="Red and white biomass pellet boiler unit"></div>

  <div class="fire-photo" role="img" aria-label="Wood pellets in the foreground with flames rising behind"></div>
  <div class="company-mark">
    <span class="dot"></span>
    <span class="name">Drumlin heating company</span>
  </div>
</main>
</body>
</html>
```